Attention grabbing 6x9 postcard

We are looking to have an attention grabbing post card that be sent out to homeowners from our roofing company Olum Roofing. the concept is that on the front it will say something like (STOP THE KNOCKING!
Tired of roofers knocking on your door? Contact us because we value your time as much as you value the roof over your head."
Olum Roofing
OlumRoofing.com
877.612.OLUM
info@olumroofing.com

Please feel free to come up with something very creative. Once we pick the final design we will provide the copy.

```html
<!DOCTYPE html>
<html lang="en">
<head>
<meta charset="utf-8">
<title>Olum Roofing – Postcard</title>
<link rel="stylesheet" href="https://fonts.googleapis.com/css2?family=Montserrat:wght@600;700&family=Didact+Gothic&display=swap">
<style>
  :root {
    --backdrop: #e8e7e5;
    --ink: #111111;
    --honey: #e0ad3b;
    --honey-deep: #d9a433;
    --cream: #f6f5e6;
    --paper-mist: #e6e6e8;
    --white: #ffffff;
    --dusk-top: #d7a6b4;
    --dusk-mid: #8a8076;
    --lawn: #6f7a4c;
  }
  * { margin: 0; padding: 0; box-sizing: border-box; }
  html, body {
    width: 1200px; height: 800px; overflow: hidden;
    background: var(--backdrop);
    font-family: "Didact Gothic", sans-serif;
  }
  .canvas { position: relative; width: 1200px; height: 800px; }

  .postcard {
    position: absolute; top: 124px;
    width: 513px; height: 364px;
    background: var(--ink);
    overflow: hidden;
  }
  .postcard--front { left: 51px; }
  .postcard--back { left: 631px; }

  /* Front */
  .front__photo {
    position: absolute; left: 0; top: 10px; width: 513px; height: 196px;
    background: linear-gradient(180deg, var(--dusk-top) 0%, #b59a9c 28%, var(--dusk-mid) 62%, #6c655d 86%, var(--lawn) 100%);
  }
  .front__brand {
    position: absolute; right: 9px; top: 54px;
    display: flex; align-items: center; gap: 6px;
    font-family: "Montserrat", sans-serif; font-weight: 700;
    font-size: 7.5px; letter-spacing: 0.18em; color: var(--white);
  }
  .front__brand-dot { width: 9px; height: 9px; border-radius: 50%; background: var(--white); }
  .front__headline-band {
    position: absolute; left: 0; top: 206px; width: 513px; height: 58px;
    background: var(--cream);
    display: flex; align-items: center; justify-content: center;
  }
  .front__headline {
    font-family: "Montserrat", sans-serif; font-weight: 700;
    font-size: 27px; letter-spacing: 0.24em; color: var(--ink);
    padding-left: 0.24em;
  }
  .front__message-band {
    position: absolute; left: 0; top: 264px; width: 513px; height: 90px;
    background: var(--honey);
    text-align: center; padding-top: 14px;
  }
  .front__question {
    font-family: "Montserrat", sans-serif; font-weight: 600;
    font-size: 14px; letter-spacing: 0.04em; color: var(--cream);
  }
  .front__body {
    margin-top: 9px; font-size: 13.5px; line-height: 16px;
    letter-spacing: 0.06em; color: #2a2418;
  }

  /* Back */
  .back__brand-panel {
    position: absolute; left: 0; top: 10px; width: 253px; height: 343px;
    background: linear-gradient(180deg, #e2b03e 0%, #ddaa3a 55%, #d6a43c 100%);
    text-align: center;
  }
  .back__mark {
    position: absolute; left: 106px; top: 70px;
    width: 42px; height: 42px; border-radius: 50%;
    border: 3px solid #1c1a17;
  }
  .back__name {
    position: absolute; left: 0; width: 100%; top: 168px;
    font-family: "Montserrat", sans-serif; font-weight: 700;
    font-size: 19px; letter-spacing: 0.14em; color: #1c1a17;
  }
  .back__rule {
    position: absolute; left: 107px; top: 203px; width: 42px; height: 2px;
    background: var(--white);
  }
  .back__subname {
    position: absolute; left: 0; width: 100%; top: 218px;
    font-family: "Montserrat", sans-serif; font-weight: 600;
    font-size: 13.5px; color: #1c1a17;
  }
  .back__contact {
    position: absolute; left: 0; width: 100%; top: 258px;
    font-size: 8px; line-height: 11.5px; letter-spacing: 0.08em; color: #1c1a17;
  }
  .back__address-panel {
    position: absolute; left: 260px; top: 10px; width: 254px; height: 343px;
    background: linear-gradient(180deg, #e9e8ec 0%, #e3e2e3 50%, #e7e6e4 100%);
  }
  .back__stamp {
    position: absolute; left: 170px; top: 33px; width: 57px; height: 70px;
    background: var(--honey);
  }
  .back__address-line {
    position: absolute; left: 39px; width: 188px; height: 2.5px;
    background: var(--honey);
  }
</style>
</head>
<body>
<main class="canvas">

  <section class="postcard postcard--front" aria-label="Postcard front">
    <div class="front__photo" role="img" aria-label="Photo of a two-storey craftsman house with garages at dusk under a pink sky"></div>
    <div class="front__brand"><span class="front__brand-dot"></span>OLUM ROOFING</div>
    <div class="front__headline-band">
      <h1 class="front__headline">STOP THE KNOCKING!</h1>
    </div>
    <div class="front__message-band">
      <p class="front__question">TIRED OF ROOFERS KNOCKING ON YOUR DOOR?</p>
      <p class="front__body">Contact us because we value your time as much as you<br>value the roof over your head.</p>
    </div>
  </section>

  <section class="postcard postcard--back" aria-label="Postcard back">
    <div class="back__brand-panel" role="img" aria-label="Faded house photo under a honey-yellow tint">
      <span class="back__mark"></span>
      <h2 class="back__name">OLUM ROOFING</h2>
      <span class="back__rule"></span>
      <p class="back__subname">OLUM ROOFING</p>
      <p class="back__contact">877.612.OLUM<br>info@olumroofing.com | www.OlumRoofing.com</p>
    </div>
    <div class="back__address-panel" role="img" aria-label="Faded house photo behind the mailing area">
      <span class="back__stamp"></span>
      <span class="back__address-line" style="top:208px"></span>
      <span class="back__address-line" style="top:232px"></span>
      <span class="back__address-line" style="top:255px"></span>
      <span class="back__address-line" style="top:279px"></span>
      <span class="back__address-line" style="top:303px"></span>
    </div>
  </section>

</main>
</body>
</html>
```